Varbelot Glues

Website for funeral directors see the original website: http://colles-varbelot.be
Target Market(s)
B2C
Coding
Coded - Design and coding required
Number of Pages Required
5+ page
Font styles to use
Serif
Sans Serif
Script
Colors
9d9d9d
757575
e667a6
eea4c8
e34197
Requirements
Must have
- Keep the architecture of the current site.
Nice to have
- A page with a list of people who have died. See example: https://www.brumejardin.be

```html
<!DOCTYPE html>
<html lang="en">
<head>
<meta charset="utf-8">
<title>Brisart &amp; Varbelot Funérailles</title>
<link rel="stylesheet" href="https://fonts.googleapis.com/css2?family=Merriweather+Sans:wght@300;400;700;800&family=Lato:wght@300;400;700&display=swap">
<style>
:root{
  --header:#57524c;
  --pink:#e667a6;
  --pink-soft:#eea4c8;
  --ink:#222;
  --grey:#757575;
  --grey-light:#9d9d9d;
  --cream:#f5f2ea;
  --teal:#1a8a7a;
  --footer:#0b0b0b;
  --white:#fff;
}
*{margin:0;padding:0;box-sizing:border-box}
html,body{width:1200px;height:4059px;overflow:hidden}
body{position:relative;font-family:"Lato",sans-serif;color:var(--ink);background:var(--white)}
.abs{position:absolute}
.heading{font-family:"Merriweather Sans",sans-serif;font-weight:800;color:#1c1c1c}
.btn{position:absolute;background:var(--pink);color:var(--white);font-family:"Merriweather Sans",sans-serif;font-weight:700;font-size:16px;display:flex;align-items:center;justify-content:center;text-transform:uppercase}

/* header */
.site-header{position:absolute;left:0;top:0;width:1200px;height:128px;background:var(--header);color:var(--white)}
.brand{position:absolute;left:110px;top:22px;display:flex;align-items:center;gap:14px;font-family:"Lato",sans-serif;font-weight:700;font-size:21px}
.brand .mark{width:44px;height:44px;border-radius:50%;border:2px solid var(--white)}
.contact-top{position:absolute;top:22px;display:flex;align-items:center;gap:14px;font-size:19px}
.contact-top .ico{width:32px;height:32px;border-radius:50%;background:var(--pink);display:flex;align-items:center;justify-content:center}
.nav{position:absolute;top:84px;left:343px;display:flex;gap:30px;font-size:16px}

/* hero */
.hero{position:absolute;left:0;top:128px;width:1200px;height:597px;background:linear-gradient(180deg,#4b4641 0%,#3a3631 45%,#1f1d1b 75%,#2d2a27 100%)}
.hero h1{position:absolute;left:0;top:178px;width:1200px;text-align:center;font-family:"Merriweather Sans",sans-serif;font-weight:700;font-size:39px;line-height:51px;color:var(--white)}
.dots span{position:absolute;left:1124px;width:12px;height:12px;border-radius:50%;background:var(--white)}
.torn{position:absolute;left:0;top:660px}

/* welcome */
.welcome-photo{left:69px;top:841px;width:465px;height:309px;background:linear-gradient(135deg,#6d8a4a,#e6e2d2 50%,#55703a)}
.welcome h2{position:absolute;left:657px;top:848px;font-size:34px}
.welcome .sub{position:absolute;left:659px;top:893px;font-size:34px;font-weight:300;color:#444;font-family:"Lato",sans-serif}
.welcome p{position:absolute;left:667px;top:947px;width:400px;font-size:14px;line-height:28.5px;color:#555}

/* deaths */
.deaths{position:absolute;left:0;top:1254px;width:1200px;height:606px;background:var(--cream)}
.section-title{position:absolute;left:0;width:1200px;text-align:center;font-size:40px}
.divider{position:absolute;left:488px;width:224px;height:14px}
.person .photo{position:absolute;width:189px;height:163px;background:linear-gradient(160deg,#b7ada0,#6a5f55)}
.person .name{position:absolute;font-family:"Merriweather Sans",sans-serif;font-weight:700;font-size:16px}
.person .dates{position:absolute;font-size:14px;color:var(--teal)}
.person .bio{position:absolute;width:213px;font-size:13.5px;line-height:19.5px;color:#444;text-align:justify}

/* flowers */
.flowers{left:0;top:1860px;width:1200px;height:428px;background:linear-gradient(120deg,#6f7a3c,#d9c36a 40%,#f0dc7a 60%,#8a7a3a)}
.flowers-box{position:absolute;left:225px;top:1955px;width:750px;height:237px;background:rgba(250,244,222,.78);text-align:center}
.flowers-box h2{margin-top:38px;font-size:33px}
.flowers-box p{margin:14px auto 0;width:420px;font-size:13px;line-height:26px;color:#777}
.more{font-family:"Merriweather Sans",sans-serif;font-weight:700;font-size:16px;color:#333;display:inline-flex;align-items:center;gap:6px}

/* services */
.service{position:absolute;width:416px;height:181px;background:var(--white);box-shadow:0 0 0 1px #e4e4e4,2px 3px 6px rgba(0,0,0,.12)}
.service .photo{position:absolute;left:0;top:0;width:178px;height:181px}
.service h3{position:absolute;left:191px;top:44px;font-family:"Merriweather Sans",sans-serif;font-size:17px;font-weight:700}
.service p{position:absolute;left:193px;top:78px;width:205px;font-size:13px;line-height:24px;color:var(--grey-light)}
.service .more{position:absolute;left:195px;top:136px;font-size:13.5px}

/* blog */
.blog{position:absolute;left:0;top:2914px;width:1200px;height:664px;background:var(--cream)}
.post{position:absolute;width:307px}
.post .photo{height:194px}
.post .date{position:absolute;left:2px;top:220px;width:38px;height:38px;background:var(--pink);color:var(--white);font-size:12px;line-height:14px;text-align:center;padding-top:5px}
.post h3{position:absolute;left:56px;top:214px;width:251px;font-family:"Merriweather Sans",sans-serif;font-weight:700;font-size:17.5px;line-height:25px}
.post p{position:absolute;left:0;top:281px;width:307px;font-size:14px;line-height:26px;color:#666}
.post .read{position:absolute;left:2px;top:371px;width:142px;height:44px;border:2px solid #333;display:flex;align-items:center;justify-content:center;font-family:"Merriweather Sans",sans-serif;font-size:14px;color:#222}
.silhouette{left:930px;top:3418px;width:270px;height:160px;background:linear-gradient(180deg,rgba(40,40,40,0) 0%,rgba(40,40,40,.75) 60%,#2a2a2a 100%)}

/* footer */
.site-footer{position:absolute;left:0;top:3578px;width:1200px;height:481px;background:var(--footer);color:var(--white)}
.site-footer .brand{left:105px;top:84px}
.footer-about{position:absolute;left:111px;top:168px;width:320px;font-size:13.5px;line-height:26px}
.site-footer h4{position:absolute;top:70px;font-family:"Merriweather Sans",sans-serif;font-weight:700;font-size:24px}
.news-text{position:absolute;left:507px;top:118px;width:280px;font-size:13px;line-height:24px}
.news-input{position:absolute;left:505px;top:172px;width:275px;height:40px;border:2px solid var(--white);border-radius:20px;font-size:11px;padding:12px 22px}
.news-btn{left:507px;top:224px;width:145px;height:38px;border-radius:19px;font-size:14px}
.c-row{position:absolute;left:842px;display:flex;gap:18px;font-size:13.5px;line-height:24px}
.c-row svg{flex:none;margin-top:3px}
.socials span{position:absolute;top:3923px;width:38px;height:38px;border:2px solid var(--white);border-radius:50%}
.copy{position:absolute;left:110px;top:4002px;color:var(--white);font-size:14px}
</style>
</head>
<body>

<header class="site-header">
  <div class="brand"><span class="mark"></span>Brisart &amp; Varbelot Funérailles</div>
  <div class="contact-top" style="left:672px">
    <span class="ico"><svg width="16" height="12" viewBox="0 0 16 12"><rect x="1" y="1" width="14" height="10" fill="none" stroke="#fff" stroke-width="1.5"/><path d="M1 1l7 6 7-6" fill="none" stroke="#fff" stroke-width="1.5"/></svg></span>contact@pfbv.be
  </div>
  <div class="contact-top" style="left:870px">
    <span class="ico"><svg width="14" height="14" viewBox="0 0 24 24"><path d="M6.6 10.8a15 15 0 0 0 6.6 6.6l2.2-2.2a1 1 0 0 1 1-.3 11 11 0 0 0 3.6.6 1 1 0 0 1 1 1V20a1 1 0 0 1-1 1A17 17 0 0 1 3 4a1 1 0 0 1 1-1h3.5a1 1 0 0 1 1 1 11 11 0 0 0 .6 3.6 1 1 0 0 1-.3 1z" fill="#fff"/></svg></span>+32 (0) 61 / 40.18.73
  </div>
  <nav class="nav"><span>Home</span><span>Our society</span><span>What to do in case of death?</span><span>Our services</span><span>They have left us</span><span>Contact</span></nav>
</header>

<section class="hero" role="img" aria-label="Black hearse parked in front of a stone church">
  <h1>He tree owes the beauty of its fruits to the<br>strength of its bark</h1>
  <div class="btn" style="left:520px;top:307px;width:167px;height:50px">Learn more</div>
  <div class="dots"><span style="top:272px;width:16px;height:16px;left:1122px;background:none;border:3px solid #fff"></span><span style="top:300px"></span><span style="top:322px"></span></div>
</section>
<svg class="torn" width="1200" height="66" viewBox="0 0 1200 66"><path d="M0 24l18-8 14 10 20-14 16 12 22-6 18 10 24-12 20 8 16-4 22 12 20-10 18 6 24-12 20 14 18-6 22 8 16-12 24 10 20-4 18 8 22-14 16 10 24-6 20 12 18-10 22 6 16-8 24 12 20-10 18 6 22-4 16 10 24-14 20 8 18-6 22 12 16-8 24 4 20 10 18-12 22 6 16 8 24-10 20 4 18 10 22-12 16 6 24 8 20-10 18 4 22 10 16-12 24 6 20 8 18-10 22 4 16 12 24-8 20 6 18-10 22 8 16-4 24 10 20-12 18 8 22-6 16 10 24-8 20 6 18 4 V66 H0z" fill="#fff"/></svg>

<section class="welcome">
  <div class="abs welcome-photo" role="img" aria-label="Funeral wreath of white gerberas and roses with a ribbon"></div>
  <h2 class="heading">WELCOME TO</h2>
  <div class="sub">brisart-varbelot</div>
  <p>A fully equipped funeral home in the city center of Beaumont, with a large private parking. In addition, we benefit from a complete infrastructure for the preparation and reception of the deceased: a treatment room adapted</p>
  <div class="btn" style="left:668px;top:1080px;width:134px;height:40px">Learn more</div>
</section>

<section class="deaths">
  <h2 class="heading section-title" style="top:62px">LATEST DEATHS</h2>
  <svg class="divider" style="top:124px" viewBox="0 0 224 14"><line x1="0" y1="7" x2="72" y2="7" stroke="#999"/><line x1="152" y1="7" x2="224" y2="7" stroke="#999"/><circle cx="112" cy="7" r="4" fill="none" stroke="#999"/></svg>

  <div class="person">
    <div class="photo" style="left:115px;top:186px" role="img" aria-label="Portrait of Lucie Hennard"></div>
    <div class="name" style="left:328px;top:188px">Lucie Hennard</div>
    <div class="dates" style="left:328px;top:217px">March 30, 1949 - May 4, 2019</div>
    <div class="bio" style="left:328px;top:248px">Lorem ipsum dolor sit amet, consectetur adipiscing elit, sed do eiusmod tempor incididunt ut sed do eiusmod tempor incididunt ut</div>
  </div>
  <div class="person">
    <div class="photo" style="left:647px;top:186px" role="img" aria-label="Portrait of Odile Verbeke"></div>
    <div class="name" style="left:860px;top:188px">Odile Verbeke</div>
    <div class="dates" style="left:860px;top:217px">December 9, 1926 - June 07, 2019</div>
    <div class="bio" style="left:862px;top:248px">Lorem ipsum dolor sit amet, consectetur adipiscing elit, sed do eiusmod tempor incididunt ut sed do eiusmod tempor incididunt ut</div>
  </div>
  <div class="person">
    <div class="photo" style="left:115px;top:386px" role="img" aria-label="Portrait of Marcel Antoine Dujardin"></div>
    <div class="name" style="left:328px;top:388px">Marcel Antoine Dujardin</div>
    <div class="dates" style="left:328px;top:417px">March 5, 1931 - May 2, 2019</div>
    <div class="bio" style="left:328px;top:448px">Lorem ipsum dolor sit amet, consectetur adipiscing elit, sed do eiusmod tempor incididunt ut sed do eiusmod tempor incididunt ut</div>
  </div>
  <div class="person">
    <div class="photo" style="left:647px;top:386px" role="img" aria-label="Portrait of Henri Lamotte"></div>
    <div class="name" style="left:860px;top:388px">Henri Lamotte</div>
    <div class="dates" style="left:860px;top:417px">December 9, 1935 - June 07, 2019</div>
    <div class="bio" style="left:862px;top:448px">Lorem ipsum dolor sit amet, consectetur adipiscing elit, sed do eiusmod tempor incididunt ut sed do eiusmod tempor incididunt ut</div>
  </div>
</section>

<section>
  <div class="abs flowers" role="img" aria-label="Yellow roses laid on a coffin"></div>
  <div class="flowers-box">
    <h2 class="heading">HAVE YOUR FLOWERS DELIVERED ONLINE</h2>
    <p>Nemo enim ipsam voluptatem quia voluptas sit aspernatur aut odit aut fugit, sed quia consequuntur magni dolores eos qui ratione</p>
    <div class="more" style="margin-top:14px">More Info <svg width="24" height="10" viewBox="0 0 24 10"><path d="M0 5h22M17 1l5 4-5 4" fill="none" stroke="#333" stroke-width="1.5"/></svg></div>
  </div>
</section>

<section>
  <h2 class="heading section-title" style="top:2355px;font-size:36px">OUR&nbsp; SERVICES</h2>
  <div class="service" style="left:175px;top:2468px">
    <div class="photo" style="background:linear-gradient(135deg,#eee,#222 55%,#b22)" role="img" aria-label="Red rose on piano keys"></div>
    <h3>Order Your Flowers online</h3>
    <p>To pay a last tribute to your loved one, offer him a personalized</p>
    <div class="more">More Info <svg width="22" height="10" viewBox="0 0 24 10"><path d="M0 5h22M17 1l5 4-5 4" fill="none" stroke="#333" stroke-width="1.5"/></svg></div>
  </div>
  <div class="service" style="left:616px;top:2468px">
    <div class="photo" style="background:linear-gradient(135deg,#4d6b35,#e88ab0 50%,#f3d3de)" role="img" aria-label="Bouquet of pink gerberas"></div>
    <h3>Embalming</h3>
    <p>To pay a last tribute to your loved one, offer him a personalized</p>
    <div class="more">More Info <svg width="22" height="10" viewBox="0 0 24 10"><path d="M0 5h22M17 1l5 4-5 4" fill="none" stroke="#333" stroke-width="1.5"/></svg></div>
  </div>
  <div class="service" style="left:175px;top:2674px">
    <div class="photo" style="background:linear-gradient(180deg,#d8641c,#f09033 55%,#4a1e0c)" role="img" aria-label="Sunset over the sea"></div>
    <h3>Funeral Insurance</h3>
    <p>The registration of your last wishes is an official act, which</p>
    <div class="more">More Info <svg width="22" height="10" viewBox="0 0 24 10"><path d="M0 5h22M17 1l5 4-5 4" fill="none" stroke="#333" stroke-width="1.5"/></svg></div>
  </div>
  <div class="service" style="left:616px;top:2674px">
    <div class="photo" style="background:linear-gradient(135deg,#cfc7bd,#6e655c)" role="img" aria-label="Black and white family photograph"></div>
    <h3 style="top:30px">Printed Mouring</h3>
    <p style="top:80px">Opt for death insurance and pay for your funeral in advance to</p>
    <div class="more">More Info <svg width="22" height="10" viewBox="0 0 24 10"><path d="M0 5h22M17 1l5 4-5 4" fill="none" stroke="#333" stroke-width="1.5"/></svg></div>
  </div>
</section>

<section class="blog">
  <h2 class="heading section-title" style="top:56px;font-size:36px">LATEST BLOG</h2>
  <article class="post" style="left:112px;top:163px">
    <div class="photo" style="background:linear-gradient(180deg,#b8d4ea,#3a9ad6 45%,#3b3b3b 75%,#7a8a5a)" role="img" aria-label="Mourners gathered under a blue tent at a cemetery"></div>
    <div class="date">07<br>Jun</div>
    <h3>Sed ut perspiciatis unde omnis iste natus error sit</h3>
    <p>Lorem ipsum dolor sit amet, consectetur adipi-sicing elit, sed do eiusmod tempor incididunt ut labore et dolore.</p>
    <div class="read">READ MORE</div>
  </article>
  <article class="post" style="left:446px;top:163px">
    <div class="photo" style="background:linear-gradient(135deg,#c27a3a,#7a3a1a 50%,#b0322a)" role="img" aria-label="Coffin with red roses in a chapel"></div>
    <div class="date">07<br>Jun</div>
    <h3>Sed ut perspiciatis unde omnis iste natus error sit</h3>
    <p>Lorem ipsum dolor sit amet, consectetur adipi-sicing elit, sed do eiusmod tempor incididunt ut labore et dolore.</p>
    <div class="read">READ MORE</div>
  </article>
  <article class="post" style="left:780px;top:163px">
    <div class="photo" style="background:linear-gradient(135deg,#d01a14,#f2562a 50%,#8a0a08)" role="img" aria-label="Red memorial candles burning"></div>
    <div class="date">07<br>Jun</div>
    <h3>Sed ut perspiciatis unde omnis iste natus error sit</h3>
    <p>Lorem ipsum dolor sit amet, consectetur adipi-sicing elit, sed do eiusmod tempor incididunt ut labore et dolore.</p>
    <div class="read">READ MORE</div>
  </article>
</section>
<div class="abs silhouette" role="img" aria-label="Silhouette of a tree above a graveyard"></div>

<footer class="site-footer">
  <div class="brand"><span class="mark"></span>Brisart &amp; Varbelot Funérailles</div>
  <p class="footer-about">Nemo enim ipsam voluptatem quia voluptas sit as-pernatur aut odit aut fugit, sed quia consequuntur magni dolores eos qui ratione voluptatem sequi ne-sciunt. Neque porro quisquam est, qui dolorem ipsum quia dolor sit amet, consectetur, adipisci</p>

  <h4 style="left:507px">Sign Up For Newsletter</h4>
  <p class="news-text">excepteur sint occaecat cupidatat non proident, sunt in culpa qui officia deserunt</p>
  <div class="news-input">Enter email</div>
  <div class="btn news-btn">Subscribe</div>

  <h4 style="left:842px">Contact Us</h4>
  <div class="c-row" style="top:124px"><svg width="14" height="18" viewBox="0 0 14 18"><path d="M7 0a7 7 0 0 0-7 7c0 5 7 11 7 11s7-6 7-11a7 7 0 0 0-7-7zm0 10a3 3 0 1 1 0-6 3 3 0 0 1 0 6z" fill="#fff"/></svg><span>rue des Tilleuls 48<br>6720 HABAY</span></div>
  <div class="c-row" style="top:190px"><svg width="16" height="16" viewBox="0 0 24 24"><path d="M6.6 10.8a15 15 0 0 0 6.6 6.6l2.2-2.2a1 1 0 0 1 1-.3 11 11 0 0 0 3.6.6 1 1 0 0 1 1 1V20a1 1 0 0 1-1 1A17 17 0 0 1 3 4a1 1 0 0 1 1-1h3.5a1 1 0 0 1 1 1 11 11 0 0 0 .6 3.6 1 1 0 0 1-.3 1z" fill="#fff"/></svg><span>Phone:<br>+32 (0) 61 / 40.18.73</span></div>
  <div class="c-row" style="top:252px"><svg width="16" height="12" viewBox="0 0 16 12"><rect x="0" y="0" width="16" height="12" fill="#fff"/><path d="M0 0l8 6 8-6" fill="none" stroke="#0b0b0b" stroke-width="1.5"/></svg><span>Email:<br>contact@pfbv.be</span></div>
</footer>
<div class="socials"><span style="left:509px"></span><span style="left:553px"></span><span style="left:600px"></span><span style="left:646px"></span></div>
<div class="copy">© 2019 Copyrights Company Name | All Rights Reserved</div>

</body>
</html>
```